The Larkspur Bay Clinic Flyer Design

The Larkspur Bay Clinic is a new company providing Dietetic services for people with gastrointestinal disorders. The main client base would be people suffering from Irritable Bowel Syndrome. IBS is a collection of symptoms which (will be individual to the suffer) including constipation/diarrhoea/abdominal pain or discomfort/bloating/belching/flatulence/stomach gurgling/reflux/nausea/urgency/incomplete emptying/fatigue/headaches. IBS affects approx 30% of the population. Previous treatments have generally been ineffectual and include medication, hypnotherapy, healthy eating.
Recently it has been found that the FODMAP diet (a diet low in fermentable Carbohydrates) has been effective in 75% of sufferers.
The Low FODMAP diet is complex and it is highly recommended that it is undertaken only under the supervision of a suitably qualified dietitian. Treatment is available within the QWR but is usually accessible only following consultation with a Gastroenterologist. Most GP's have never heard of this treatment as the research was only published in 2009 in Australia and is yet to filter through to the general practitioner. The Larkspur Bay Clinic is the only clinic in the UK offering dietetic lead specialist services.
I am a member of the KSL and RWMT (logos provided)
The flyer would be double sided, informing the patient of all the self help steps they could take if they have IBS then recommending that they contact The Larkspur Bay Clinic for specialist advice.
Self Help: Healthy eating, regular meals, good intake of non caffeinated non alcoholic non fizzy drinks, regular exercise, stress management.
The flyer would be left in GP surgeries, Health centres, holistic therapy centres, or through doors.
Majority female aged 20-50, able to pay for private services
Clinic

```html
<!DOCTYPE html>
<html lang="en">
<head>
<meta charset="utf-8">
<title>The Larkspur Bay Clinic – Flyer</title>
<link rel="stylesheet" href="https://fonts.googleapis.com/css2?family=Roboto:wght@300;400&family=Roboto+Condensed:wght@300;400&family=Tenor+Sans&display=swap">
<style>
  :root {
    --white: #ffffff;
    --ink: #111111;
    --grey-text: #8f9396;
    --heading-grey: #3f4346;
    --deep-blue: #17496b;
    --cyan: #1fb4e9;
    --cyan-soft: #c9ecfa;
    --we-ink: #1f3140;
    --badge-navy: #1b3f73;
  }
  * { margin: 0; padding: 0; box-sizing: border-box; }
  html, body { width: 1200px; height: 851px; overflow: hidden; background: var(--white); }
  .flyer {
    position: relative; width: 1200px; height: 851px; overflow: hidden;
    background: var(--white); font-family: "Roboto", Arial, sans-serif;
  }
  .backdrop { position: absolute; left: 0; top: 0; width: 1200px; height: 851px; }

  .brand {
    position: absolute; left: 150px; top: 78px;
    font-family: "Tenor Sans", Georgia, serif; font-weight: 400; color: var(--ink);
    line-height: 1;
  }
  .brand-line-small { display: block; font-size: 31px; }
  .brand-line-large { display: block; font-size: 45px; margin-top: 4px; }
  .brand-mark {
    position: absolute; left: 56px; top: 84px; width: 76px; height: 76px;
    border: 2px solid var(--ink); border-radius: 50%;
  }

  .symptom-question {
    position: absolute; left: 58px; top: 222px; width: 320px; text-align: center;
    font-weight: 300; font-size: 23px; line-height: 29px; color: var(--grey-text);
  }
  .symptom-question .accent { color: var(--cyan); font-weight: 400; }

  .symptom {
    position: absolute; width: 150px; text-align: center;
    font-weight: 300; font-size: 19px; line-height: 24px; color: var(--cyan);
  }
  .symptom-icon {
    display: block; width: 56px; height: 58px; margin: 0 auto;
    border-radius: 14px; background: var(--cyan-soft);
  }
  .symptom-label { display: block; }

  .headline {
    position: absolute; right: 327px; top: 118px; text-align: right;
    font-family: "Roboto Condensed", Arial, sans-serif; font-weight: 300;
    white-space: nowrap;
  }
  .headline-top { display: block; font-size: 47px; line-height: 54px; color: var(--heading-grey); }
  .headline-main { display: block; font-size: 45px; line-height: 56px; color: var(--deep-blue); }

  .ibs-intro {
    position: absolute; right: 327px; top: 242px; text-align: right; white-space: nowrap;
    font-weight: 300; font-size: 14.8px; line-height: 19.2px; color: var(--cyan);
  }

  .claim {
    position: absolute; left: 462px; top: 495px;
    font-family: "Roboto Condensed", Arial, sans-serif; font-weight: 300; color: var(--we-ink);
  }
  .claim-lead { display: block; font-size: 46px; line-height: 50px; }
  .claim-line { display: block; font-size: 20px; line-height: 28.6px; }

  .membership { position: absolute; top: 784px; left: 0; width: 0; height: 0; }
  .badge { position: absolute; }
  .badge-dietitians { left: 279px; top: 4px; width: 62px; height: 26px; background: var(--cyan); border-radius: 3px; }
  .badge-register { left: 428px; top: 0; width: 46px; height: 44px; background: var(--badge-navy); }
</style>
</head>
<body>
<main class="flyer">
  <svg class="backdrop" viewBox="0 0 1258 892" preserveAspectRatio="none" role="img" aria-label="Photograph of a young woman in a grey vest top holding her stomach in discomfort, in a bright blurred kitchen">
    <defs>
      <linearGradient id="photo-tone" x1="0" y1="0" x2="1" y2="1">
        <stop offset="0" stop-color="#f3f5f7"/>
        <stop offset="0.6" stop-color="#e2e7eb"/>
        <stop offset="1" stop-color="#d0d8de"/>
      </linearGradient>
    </defs>
    <path class="photo-area" d="M590,0 L1258,0 L1258,892 L720,892 C715,820 705,740 690,650 C670,560 600,480 560,380 C525,250 545,120 590,0 Z" fill="url(#photo-tone)"/>
    <path class="band-light" d="M690,650 C800,740 1000,800 1258,820 L1258,892 L720,892 C715,820 705,740 690,650 Z" fill="#5fcbf1"/>
    <path class="band-dark" d="M455,0 L590,0 C545,120 525,250 560,380 C600,480 670,560 690,650 C705,740 715,820 720,892 L655,892 C655,850 656,780 650,680 C640,580 565,470 500,380 C450,300 435,150 455,0 Z" fill="#38393c"/>
    <path class="band-blue" d="M452,260 C440,400 450,560 520,700 C570,800 620,860 650,892 L655,892 C655,850 656,780 650,680 C640,580 565,470 500,380 C475,340 460,300 452,260 Z" fill="#07b6ea"/>
  </svg>

  <span class="brand-mark" aria-hidden="true"></span>
  <h1 class="brand">
    <span class="brand-line-small">The Larkspur Bay</span>
    <span class="brand-line-large">Clinic</span>
  </h1>

  <p class="symptom-question">Are you suffering from<br>all these <span class="accent">symptoms</span> below?</p>

  <div class="symptom" style="left:73px;top:300px;">
    <span class="symptom-icon" role="img" aria-label="Icon of a person on a toilet"></span>
    <span class="symptom-label" style="margin-top:10px;">Constipation/<br>Diarrhoea</span>
  </div>
  <div class="symptom" style="left:219px;top:300px;">
    <span class="symptom-icon" role="img" aria-label="Icon of a mouth releasing air"></span>
    <span class="symptom-label" style="margin-top:10px;">Belching/<br>Burping</span>
  </div>
  <div class="symptom" style="left:73px;top:437px;">
    <span class="symptom-icon" role="img" aria-label="Icon of a bending person passing wind"></span>
    <span class="symptom-label" style="margin-top:29px;">Flatulence</span>
  </div>
  <div class="symptom" style="left:219px;top:437px;">
    <span class="symptom-icon" role="img" aria-label="Icon of a person holding their stomach"></span>
    <span class="symptom-label" style="margin-top:29px;">Indigestion/<br>Reflux</span>
  </div>
  <div class="symptom" style="left:73px;top:590px;">
    <span class="symptom-icon" role="img" aria-label="Icon of a slumped tired person"></span>
    <span class="symptom-label" style="margin-top:28px;">Fatigue/ Tired<br>all the time</span>
  </div>
  <div class="symptom" style="left:219px;top:590px;">
    <span class="symptom-icon" role="img" aria-label="Icon of a seated person holding their head"></span>
    <span class="symptom-label" style="margin-top:28px;">Headaches/<br>Low mood</span>
  </div>

  <h2 class="headline">
    <span class="headline-top">What’s your</span>
    <span class="headline-main">Gut feeling now?</span>
  </h2>

  <p class="ibs-intro">You would be suffering from Irritable Bowel<br>Syndrome(IBS).<br>IBS is a collection of symptoms which<br>including constipation/ diarrhoea/ abdominal<br>pain or discomfort/ bloating/ belching/<br>flatulence/ stomach gurgling/ reflux/ nausea/<br>urgency/ incomplete emptying/ fatigue/<br>headaches.</p>

  <p class="claim">
    <span class="claim-lead">WE</span>
    <span class="claim-line" style="padding-left:4px;">are the only</span>
    <span class="claim-line" style="padding-left:12px;">clinic in the UK</span>
    <span class="claim-line" style="padding-left:20px;">offering dietetic</span>
    <span class="claim-line" style="padding-left:33px;">lead specialist</span>
    <span class="claim-line" style="padding-left:38px;">services.</span>
  </p>

  <div class="membership" aria-label="Professional memberships">
    <span class="badge badge-dietitians" role="img" aria-label="KSL membership badge"></span>
    <span class="badge badge-register" role="img" aria-label="RWMT registration badge"></span>
  </div>
</main>
</body>
</html>
```